Re-design web project

1.Re-design of http://www.clipmerel.example
Logo		Ons concept 	Video referenties	Pagina delen	Promoot uw bedrijfsfilm
(Our concept)	(Video references)	(Share page)	(Promote yr company video)
Share-this buttons
Content promotion float
•	Bestel vandaag uw creatieve video en wij brengen hem vanaf 0,29 EUR onder de aandacht van potentiële klanten (Order today your creative video and we promote it online towards potential customers starting from € 0.29)
Slideshow images + content
•	Social Video = Online Video + Marketing + Social Media (Social Video = Online Video + Marketing + Social Media)
•	We verbeelden uw concept in een creatieve, aansprekende video (We visualise your concept into a creative video
•	We promoten uw video online en bereiken enkel potentiële klanten (We promote your video online and reach potential customers only)
•	Onbekende prospects worden kwalitatieve leads! (Unknown prospects are quality leads!)
Sketch + content
•	We stellen u een passend scenario voor (We propose an apropriate scenrio)
•	We visualiseren uw diensten (We visualize your services)
•	We brengen uw video onder de aandacht van potentiële klanten (We bring your video under the attention of potential customers)
•	We laten uw onderneming groeien! (We let your business grow!)
Bekijk onze video (Watch our video)
Ontvang vrijblijvend een presentatie van onze dienstverlening (Get a free presentation of our services )
Een aantal van onze video projecten (Take a look at our video projects)

Sitemap    Voorwaarden    Ons team    Contact
2. Re-design of http://www.clipmerel.example/luxe-appartement-centrum-gent as well

```html
<!DOCTYPE html>
<html lang="nl">
<head>
<meta charset="utf-8">
<title>Clipmerel</title>
<link href="https://fonts.googleapis.com/css2?family=Arimo:wght@400;700&family=PT+Sans:wght@400;700&family=Tinos&display=swap" rel="stylesheet">
<style>
:root{
  --page:#ffffff;
  --stage:#f4f4f4;
  --frame:#c9c9c9;
  --ink:#222222;
  --heading:#555555;
  --link:#1a3f9c;
  --hero-top:#1b5fd2;
  --hero-bottom:#3f8ff0;
  --nav-active:#3d78e0;
  --footer:#eeeeee;
  --rule:#d6d6d6;
  --button-ink:#1d3554;
}
*{box-sizing:border-box;margin:0;padding:0}
html,body{width:1042px;height:1200px;overflow:hidden}
body{background:var(--stage);font-family:"Arimo",Arial,sans-serif;color:var(--ink);position:relative}
.page{position:absolute;left:19px;top:17px;width:1004px;height:1166px;background:var(--page);border:1px solid var(--frame);box-shadow:0 0 8px rgba(0,0,0,.35);overflow:hidden}
.abs{position:absolute}

/* header */
.brand{left:38px;top:32px;display:flex;align-items:center;gap:8px}
.brand-mark{width:38px;height:38px;border-radius:50%;background:#444}
.brand-name{font-family:"Tinos",serif;font-size:31px;line-height:30px;color:#333;letter-spacing:.5px}
.brand-caption{font-size:15px;color:#8a8a8a;line-height:16px}
.nav{top:53px;left:452px;display:flex;align-items:center;gap:24px;list-style:none}
.nav li{font-size:11px;color:#777;text-transform:uppercase;height:29px;line-height:29px;white-space:nowrap}
.nav .active{padding:0 14px;color:#fff;background:linear-gradient(#6a9cf2,var(--nav-active));border:1px solid #2a5bb8;border-radius:4px;box-shadow:0 1px 2px rgba(0,0,0,.3)}

/* hero */
.hero{left:0;top:103px;width:1004px;height:352px;background:linear-gradient(180deg,var(--hero-top),var(--hero-bottom) 80%,#5aa0f2)}
.hero-title{left:53px;top:88px;font-family:"PT Sans",sans-serif;font-weight:400;font-size:29px;line-height:36px;color:#fff;text-shadow:0 1px 2px rgba(0,0,0,.35)}
.hero-cta{left:58px;top:234px;width:269px;height:55px;border-radius:6px;background:linear-gradient(#ffffff,#dfe6ee 55%,#8fa3b8);box-shadow:0 3px 5px rgba(0,0,0,.35);font-family:"PT Sans",sans-serif;font-weight:700;font-size:20px;color:var(--button-ink);display:flex;align-items:center;justify-content:center;gap:8px;letter-spacing:.3px}
.hero-visual{left:569px;top:22px;width:342px;height:300px;border-radius:8px;background:linear-gradient(135deg,#e8d8a8,#c9c9d6 45%,#2b2b2b 75%)}

/* features */
.feature-head{display:flex;align-items:center;gap:10px}
.feature-title{font-size:26px;font-weight:700;color:var(--heading);white-space:nowrap}
.feature-text{font-size:12px;line-height:21px;color:var(--ink);width:262px}
.btn-more{width:103px;height:29px;border:1px solid #bdbdbd;border-radius:4px;background:linear-gradient(#fbfbfb,#dcdcdc);font-family:"PT Sans",sans-serif;font-weight:700;font-size:14px;color:#666;text-align:center;line-height:27px;box-shadow:0 1px 2px rgba(0,0,0,.2)}
.service-list{list-style:none;width:278px}
.service-list li{height:31px;line-height:22px;font-size:12px;color:var(--link);padding-left:18px;position:relative;border-bottom:1px dotted #777}
.service-list li:last-child{border-bottom:none}
.service-list li::before{content:"";position:absolute;left:2px;top:7px;border-left:6px solid #222;border-top:5px solid transparent;border-bottom:5px solid transparent}

/* footer */
.footer{left:0;top:845px;width:1004px;height:224px;background:var(--footer);border-top:2px solid var(--rule)}
.footer h3{font-size:16px;font-weight:700;color:var(--heading)}
.browse{list-style:none;font-size:12px;line-height:21px;color:#444}
.quote{font-size:12px;line-height:20px;color:#444;width:318px}
.quote-by{font-weight:700;color:#111;font-size:12px;line-height:15px}
.post{font-size:12px;line-height:15px;color:#444;width:300px}
.post strong{color:var(--link);display:block}
.bottom-bar{left:0;top:1069px;width:1004px;height:64px;background:var(--footer);border-top:1px solid #fff}
.social{position:absolute;top:20px;width:19px;height:19px;border-radius:3px}
</style>
</head>
<body>
<div class="page">

  <header>
    <div class="abs brand">
      <span class="brand-mark"></span>
      <div>
        <div class="brand-name">CLIPMEREL</div>
        <div class="brand-caption">Your business caption here</div>
      </div>
    </div>
    <ul class="abs nav">
      <li class="active">Ons concept</li>
      <li>Video referenties</li>
      <li>Pagina delen</li>
      <li>Promoot uw bedrijfsfilm</li>
    </ul>
  </header>

  <section class="abs hero">
    <h1 class="abs hero-title">Social Video =<br>Online Video + Marketing<br>+ Social Media</h1>
    <div class="abs hero-cta">BEKIJK ONZE VIDEO
      <svg width="22" height="14" viewBox="0 0 22 14"><path d="M0 4h12V0l10 7-10 7v-4H0z" fill="#555"/></svg>
    </div>
    <div class="abs hero-visual" role="img" aria-label="Popcorn box, clapperboard and disc illustration"></div>
  </section>

  <section>
    <div class="abs feature-head" style="left:38px;top:522px">
      <svg width="56" height="58" viewBox="0 0 56 58" aria-hidden="true">
        <path d="M20 2l8 8 8-8" stroke="#333" stroke-width="3" fill="none"/>
        <rect x="1" y="10" width="54" height="44" rx="5" fill="#333"/>
        <rect x="6" y="16" width="34" height="32" rx="3" fill="#fff"/>
        <circle cx="47" cy="20" r="3" fill="#fff"/><circle cx="47" cy="29" r="3" fill="#fff"/>
        <rect x="44" y="36" width="6" height="2" fill="#fff"/><rect x="44" y="41" width="6" height="2" fill="#fff"/>
        <rect x="6" y="54" width="6" height="4" fill="#333"/><rect x="44" y="54" width="6" height="4" fill="#333"/>
      </svg>
      <h2 class="feature-title">Ons concept</h2>
    </div>
    <p class="abs feature-text" style="left:44px;top:600px">Social Video = Online Video + Marketing + Social Media. We verbeelden uw concept in een creatieve, aansprekende video. We promoten uw video online en bereiken enkel potentiële klanten. Onbekende prospects worden kwalitatieve leads! Bestel vandaag uw video, promotie vanaf 0,29 EUR.</p>
    <div class="abs btn-more" style="left:38px;top:775px">LEES MEER</div>

    <div class="abs feature-head" style="left:366px;top:524px">
      <svg width="46" height="50" viewBox="0 0 46 50" aria-hidden="true">
        <rect x="0" y="0" width="46" height="50" fill="#333"/>
        <rect x="11" y="4" width="24" height="19" fill="#fff"/><rect x="11" y="27" width="24" height="19" fill="#fff"/>
        <g fill="#fff"><rect x="3" y="4" width="5" height="6"/><rect x="3" y="15" width="5" height="6"/><rect x="3" y="27" width="5" height="6"/><rect x="3" y="39" width="5" height="6"/>
        <rect x="38" y="4" width="5" height="6"/><rect x="38" y="15" width="5" height="6"/><rect x="38" y="27" width="5" height="6"/><rect x="38" y="39" width="5" height="6"/></g>
      </svg>
      <h2 class="feature-title">Onze aanpak</h2>
    </div>
    <p class="abs feature-text" style="left:366px;top:600px">We stellen u een passend scenario voor. We visualiseren uw diensten. We brengen uw video onder de aandacht van potentiële klanten. We laten uw onderneming groeien!</p>
    <ul class="abs service-list" style="left:366px;top:734px">
      <li>Passend scenario</li>
      <li>Creatieve video</li>
      <li>Online promotie</li>
    </ul>

    <div class="abs feature-head" style="left:680px;top:522px">
      <svg width="52" height="58" viewBox="0 0 52 58" aria-hidden="true"><circle cx="26" cy="29" r="24" fill="#333"/></svg>
      <h2 class="feature-title">Waarom wij?</h2>
    </div>
    <p class="abs feature-text" style="left:686px;top:600px">Ontvang vrijblijvend een presentatie van onze dienstverlening. Een aantal van onze video projecten toont hoe wij uw concept verbeelden en uw video online promoten bij potentiële klanten. Zo worden onbekende prospects kwalitatieve leads.</p>
    <div class="abs btn-more" style="left:684px;top:780px">LEES MEER</div>
  </section>

  <footer>
    <div class="abs footer">
      <h3 class="abs" style="left:44px;top:34px">Navigatie</h3>
      <ul class="abs browse" style="left:44px;top:72px">
        <li>Sitemap</li><li>Voorwaarden</li><li>Ons team</li><li>Contact</li><li>Video referenties</li><li>Pagina delen</li>
      </ul>

      <h3 class="abs" style="left:282px;top:34px">Getuigenissen</h3>
      <p class="abs quote" style="left:282px;top:72px">Lorem ipsum dolor sit amet, consectetur adipiscing elit. Etiam tristique tristique lacus in varius. Donec nec vestibulum ligula. Aenean turpis diam, feugiat a luctus in, rhoncus eget risus. Maecenas consequat porttitor dui, vitae consequat massa imperdiet ut. elit ut tempus lobortis, eros leo molestie velit.</p>
      <p class="abs quote-by" style="left:282px;top:196px">Joren, Studioveld.example</p>

      <h3 class="abs" style="left:669px;top:33px">Van onze blog</h3>
      <div class="abs post" style="left:669px;top:71px">July 6, 2010<strong>Lorem ipsum dolor sit amet, consectetur</strong>adipiscing elit. Etiam tristique tristique lacus in varius. Donec nec vestibulum ligula. Aenean turpis diam...</div>
      <div class="abs post" style="left:669px;top:147px">July 6, 2010<strong>Lorem ipsum dolor sit amet, consectetur</strong>adipiscing elit. Etiam tristique tristique lacus in varius. Donec nec vestibulum ligula. Aenean turpis diam...</div>
    </div>
    <div class="abs bottom-bar">
      <span class="social" style="left:672px;background:#47a9dc"></span>
      <span class="social" style="left:706px;background:#2a6aa6"></span>
      <span class="social" style="left:741px;background:#3b5a9a"></span>
    </div>
  </footer>

</div>
</body>
</html>
```